Brightbuns Business Card Design

Our company is called Brightbuns. We manufacture confectionary snacks & frozen novelties. Our initial product portfolio includes frozen ice lollies/popsicles & stick ice cream bars.

We require a business card design.

Please use the attached Logo.

Please use an orange, brown, yellow colour code. You may choose any combination of the 3 or include all three. The logo however must remain orange.

Target Market(s)

Business card will be targeted at distributors of our products such as supermarket procurement managers, convenience store owners, wholesale distributors and merchandising agents.

Industry/Entity Type

Business

Requirements
Must have
• Kelvin Marsh_Director/ P.O.Box Westhollow 5172, Accra, Ghana / m: 00233(0)507318264/ e: kelvin.marsh@fernpost.co.uk

```html
<!DOCTYPE html>
<html lang="en">
<head>
<meta charset="UTF-8">
<title>Brightbuns Business Card</title>
<link href="https://fonts.googleapis.com/css2?family=Dosis:wght@400;500;700&display=swap" rel="stylesheet">
<style>
  :root {
    --page-bg: #ffffff;
    --card-maroon: #4a1010;
    --card-maroon-light: #5e1a17;
    --sweets-tone: #6e1f1a;
    --brand-orange: #f26f21;
    --text-white: #ffffff;
  }
  * { margin: 0; padding: 0; box-sizing: border-box; }
  html, body {
    width: 1200px;
    height: 900px;
    overflow: hidden;
    background: var(--page-bg);
  }
  .canvas {
    position: relative;
    width: 1200px;
    height: 900px;
  }
  .business-card {
    position: absolute;
    left: 334px;
    top: 12px;
    width: 530px;
    height: 876px;
    background: var(--card-maroon);
    overflow: hidden;
    font-family: "Dosis", sans-serif;
    color: var(--text-white);
  }
  .sweets-backdrop {
    position: absolute;
    left: 20px;
    top: 10px;
    width: 490px;
    height: 860px;
    background:
      radial-gradient(ellipse at 55% 18%, var(--sweets-tone) 0%, transparent 45%),
      radial-gradient(ellipse at 65% 55%, var(--card-maroon-light) 0%, transparent 40%),
      radial-gradient(ellipse at 25% 70%, var(--card-maroon-light) 0%, transparent 35%);
    opacity: 0.8;
  }
  .brand-mark {
    position: absolute;
    left: 0;
    top: 215px;
    width: 100%;
    text-align: center;
  }
  .brand-dot {
    display: block;
    width: 84px;
    height: 84px;
    margin: 0 auto 14px;
    border-radius: 50%;
    background: var(--brand-orange);
  }
  .brand-name {
    font-size: 84px;
    font-weight: 700;
    line-height: 1;
    color: var(--brand-orange);
    letter-spacing: 1px;
  }
  .contact-block {
    position: absolute;
    left: 0;
    top: 568px;
    width: 100%;
    text-align: center;
  }
  .contact-name {
    font-size: 44px;
    font-weight: 500;
    line-height: 1.2;
  }
  .contact-role,
  .contact-line {
    font-size: 23px;
    font-weight: 400;
    line-height: 34px;
  }
  .contact-role { margin-top: 2px; }
</style>
</head>
<body>
<div class="canvas">
  <div class="business-card">
    <div class="sweets-backdrop" role="img" aria-label="Faint illustration of ice creams, lollies, cupcakes and sweets across the card"></div>

    <div class="brand-mark">
      <span class="brand-dot"></span>
      <div class="brand-name">Brightbuns</div>
    </div>

    <div class="contact-block">
      <div class="contact-name">Kelvin Marsh</div>
      <div class="contact-role">Director</div>
      <div class="contact-line">P.O.Box Westhollow 5172,</div>
      <div class="contact-line">Accra, Ghana</div>
      <div class="contact-line">m: 00 233 (0) 507 318 264</div>
      <div class="contact-line">e: kelvin.marsh@fernpost.co.uk</div>
    </div>
  </div>
</div>
</body>
</html>
```